HR Company Website

Home page and information page needs for Human resources company
SERVICES

Employment Law - -
HR Advice -
Recruitment -
Disciplinaries -
Redundancies -
Coaching & Training -
HR Policy Review -
Contract Writing -
Tribunal Claims -
HR Partner -

LAYOUT SKETCH DISCUSSED:
Yes
On the animation the left hand side messgae banner will be constant along with the button , the right hand side will be animated.

COMPETITION
Vantor HR - www.vantorhr-example.com
Kel HR - www.kelhr-example.co.uk
Brisk HR - www.briskhr-example.com

COMPANY LOGO
Client currently has no logo - Solvinex to design

STRAPLINE:
Brisk HR Partner

ACCREDITATIONS / LOGOS:
Masters Diploma in Emloyment Law

WEBSITE THEME:
Human Resources

MAIN BODY OF WEBSITE:
Light

IMAGES THAT BEST REFLECT YOUR COMPANY:
Staff / Office Based Life style images People groups - no face close ups
planning
infrastructure
NOTHING TOO OBVIOUS

PAGES:

Home
About Us
Our Services
- Employment Law Advice
- HR Advice
- Contracts of Employment
- HR Policies
- Disciplinary Procedures
- Redundancy Advice
Contact Us

MESSAGE BANNERS:
1. 12 Years HR Experience - wealth of experience & knowledge
2. Cost Effective Solution - use us when you need us
3. Personal HR Approach - create bespoke tailored made solutions
4. Preventative Measures Protects - don't leave it until is is too late
5. Complete Peace of Mind - Let us be Brisk HR department

Target Market(s)

Male & Femaie - 30-60

SME Business

Industry/Entity Type

Consulting

Number of Pages Required

2 pages

Requirements
Must have
• This design will be built using the wordpress platform, use the wireframe attached for the layout structure - must be visually impactful - clean and proefessional looking
Nice to have
• I have attached the logo - do not amend the colout but you can add effects onto it if you wish to
Should not have
• Loads of text

```html
<!DOCTYPE html>
<html lang="en">
<head>
<meta charset="utf-8">
<title>Corvale HR Ltd</title>
<link href="https://fonts.googleapis.com/css2?family=Mulish:wght@300;400;700&family=Noto+Sans:wght@400;700&display=swap" rel="stylesheet">
<style>
:root{
  --green:#5fb83a;
  --green-light:#9be66a;
  --green-dark:#2f8a1e;
  --heading-green:#1f7a3c;
  --ink:#3a3a3a;
  --body:#555;
  --nav:#2b2b2b;
  --nav-2:#3a3a3a;
  --frame:#e6e6e6;
  --field:#eeeeee;
}
*{box-sizing:border-box;margin:0;padding:0}
html,body{width:1200px;height:2501px;overflow:hidden;background:#fff}
body{position:relative;font-family:"Noto Sans",sans-serif;color:var(--body)}
.abs{position:absolute}
.page{position:absolute;left:10px;width:1180px;background:#fff;box-shadow:0 0 6px rgba(0,0,0,.15)}
.page-home{top:0;height:1238px}
.page-inner{top:1262px;height:1239px}
.site-header{position:absolute;left:0;top:0;width:1180px;height:143px;background:linear-gradient(#fff,#f2f2f2)}
.brand{position:absolute;left:12px;top:24px;display:flex;align-items:center;gap:10px}
.brand-mark{width:22px;height:22px;background:var(--green-dark)}
.brand-name{font-family:"Mulish",sans-serif;font-weight:700;font-size:40px;color:var(--green-dark);letter-spacing:-1px}
.brand-tag{position:absolute;left:140px;top:104px;font-family:"Mulish",sans-serif;font-weight:700;font-size:22px;color:#8bbf1e}
.call{position:absolute;right:55px;top:30px;font-family:"Mulish",sans-serif;font-size:22px;color:var(--green-dark)}
.call b{font-size:30px;font-weight:400}
.nav{position:absolute;left:346px;top:88px;width:834px;height:55px;background:linear-gradient(var(--nav-2),var(--nav));display:flex}
.nav a{color:#fff;text-decoration:none;font-family:"Mulish",sans-serif;font-size:20px;display:flex;align-items:center;justify-content:center;border-right:1px solid #555}
.nav a:last-child{border-right:0}
.hero{position:absolute;left:0;top:144px;width:1180px;height:398px;background:radial-gradient(ellipse at 35% 30%,var(--green-light),var(--green) 60%,#4aa32b)}
.hero-title{position:absolute;left:52px;top:80px;font-family:"Mulish",sans-serif;font-weight:300;font-size:44px;line-height:54px;color:#fff}
.btn-dark{position:absolute;background:linear-gradient(#3a3a3a,#222);color:#fff;font-family:"Mulish",sans-serif;font-weight:700;font-size:23px;display:flex;align-items:center;justify-content:center;border:2px solid #555;box-shadow:0 2px 4px rgba(0,0,0,.3)}
.photo-frame{position:absolute;left:608px;top:18px;width:514px;height:324px;background:#000}
.photo{position:absolute;border:3px solid #fff;border-radius:4px}
.photo-caption{position:absolute;left:0;width:514px;top:272px;text-align:center;color:#fff;font-family:"Mulish",sans-serif;font-size:20px;line-height:22px}
.card{position:absolute;top:514px;width:374px;height:242px;background:linear-gradient(#f7f7f7,#fff);border:1px solid #e2e2e2;border-radius:6px;padding:16px 16px}
.card h2{font-family:"Mulish",sans-serif;font-weight:400;font-size:22px;color:var(--heading-green);margin-bottom:14px}
.card p{font-size:12.5px;line-height:16px;letter-spacing:.5px;color:#444;margin-bottom:14px}
.testimonial{position:absolute;top:800px;left:0;width:1180px;text-align:center;font-size:13.5px;font-weight:700;color:#3ea021;letter-spacing:.6px}
.rule{position:absolute;left:0;top:826px;width:1180px;height:3px;background:var(--frame)}
.vdots{position:absolute;border-left:2px dotted #999}
.sec-title{font-family:"Mulish",sans-serif;font-size:21px;color:var(--heading-green)}
.small{font-size:12.5px;line-height:16px;letter-spacing:.5px;color:#444}
.cta-quote{font-family:"Mulish",sans-serif;font-size:21px;line-height:29px;color:var(--heading-green);text-align:center}
.btn-green{position:absolute;left:466px;top:931px;width:241px;height:69px;background:linear-gradient(var(--green-light),var(--green));border:3px solid #7ed957;color:#fff;font-family:"Mulish",sans-serif;font-size:26px;display:flex;align-items:center;justify-content:center}
.form-label{position:absolute;left:829px;font-size:12px;font-weight:700;color:#444}
.field{position:absolute;left:925px;width:199px;background:var(--field)}
.btn-small{position:absolute;top:1114px;width:93px;height:33px;border-radius:5px;background:linear-gradient(#3a3a3a,#1c1c1c);color:#fff;font-size:13px;font-weight:700;display:flex;align-items:center;justify-content:center}
.footer{position:absolute;left:0;width:1180px;height:55px;background:linear-gradient(#222 50%,#3a3a3a 50%);color:#fff;font-size:12.5px;font-weight:700;text-align:center;padding-top:26px}
.dropdown{position:absolute;left:712px;top:136px;width:228px;background:rgba(40,40,40,.92);z-index:2}
.dropdown a{display:block;height:34px;line-height:34px;padding-left:22px;color:#fff;font-family:"Mulish",sans-serif;font-size:19px;text-decoration:none;border-bottom:1px solid #555}
.article h1{font-family:"Mulish",sans-serif;font-weight:400;font-size:30px;color:var(--heading-green);margin-bottom:24px}
.article p{font-size:13px;line-height:24px;color:#666;letter-spacing:.3px;margin-bottom:24px}
.news{position:absolute;left:798px;top:410px;width:322px;height:282px;border:1px solid #bbb;background:#fff}
.news h3{height:38px;background:linear-gradient(var(--green-light),var(--green));color:#fff;font-family:"Mulish",sans-serif;font-weight:700;font-size:19px;line-height:38px;padding-left:10px}
.news ul{list-style:circle;padding:14px 0 0 42px}
.news li{font-size:13px;font-weight:700;color:#222;line-height:24px;letter-spacing:.6px;margin-bottom:16px}
.news .more{position:absolute;right:36px;bottom:10px;font-size:12px;font-weight:700;color:#222;text-decoration:underline}
</style>
</head>
<body>

<section class="page page-home">
  <header class="site-header">
    <div class="brand"><span class="brand-mark"></span><span class="brand-name">Corvale HR Ltd</span></div>
    <div class="brand-tag">Brisk HR Partner</div>
    <div class="call">Call Now: <b>000 4410 927</b></div>
    <nav class="nav">
      <a style="width:171px">HOME</a><a style="width:194px">ABOUT US</a><a style="width:231px">OUR SERVICES</a><a style="width:238px">CONTACT US</a>
    </nav>
  </header>

  <div class="hero">
    <div class="hero-title">IS YOUR COMPANY<br>LEGALLY COMPLIANT?</div>
    <div class="btn-dark" style="left:50px;top:246px;width:458px;height:60px">FREE HR AUDIT</div>
    <div class="photo-frame">
      <div class="photo" role="img" aria-label="Smiling HR consultant in an office with colleagues in the background" style="left:17px;top:12px;width:480px;height:250px;background:linear-gradient(120deg,#8a8378,#d8d2c8 45%,#f4f1ec)"></div>
      <div class="photo-caption">Over 12 years HR experience -<br>a wealth of knowledge</div>
    </div>
  </div>

  <article class="card" style="left:18px">
    <h2>Employment Law Advice</h2>
    <p>Lorem ipsum dolor sit amet, consectetur adipiscing elit. Donec nisl magna, congue id ullamcorper quis, faucibus ac diam. Mauris dictum orci vitae neque varius condimentum. Morbi venenatis fringilla risus sed iaculis.</p>
    <p>Integer luctus orci ac mauris pulvinar id lacinia lorem tincidunt. Suspendisse potenti. Vivamus nec neque sapien.</p>
  </article>
  <article class="card" style="left:403px">
    <h2>Personal HR approach</h2>
    <p>Lorem ipsum dolor sit amet, consectetur adipiscing elit. Donec nisl magna, congue id ullamcorper quis, faucibus ac diam. Mauris dictum orci vitae neque varius condimentum. Morbi venenatis fringilla risus sed iaculis.</p>
    <p>Integer luctus orci ac mauris pulvinar id lacinia lorem tincidunt. Suspendisse potenti. Vivamus nec neque sapien.</p>
  </article>
  <article class="card" style="left:788px">
    <h2>Rates &amp; Packages</h2>
    <p>Lorem ipsum dolor sit amet, consectetur adipiscing elit. Donec nisl magna, congue id ullamcorper quis, faucibus ac diam. Mauris dictum orci vitae neque varius condimentum. Morbi venenatis fringilla risus sed iaculis.</p>
    <p>Integer luctus orci ac mauris pulvinar id lacinia lorem tincidunt. Suspendisse potenti. Vivamus nec neque sapien.</p>
  </article>

  <div class="testimonial">Testimonial goes here - a very pleased client -testimonial goes here - a very pleased client</div>
  <div class="rule"></div>

  <div class="abs" style="left:36px;top:858px;width:340px">
    <div class="sec-title">CONTACT DETAILS</div>
    <div class="small" style="font-weight:700;margin:8px 0 18px">OFFICE</div>
    <div class="small">42 larkfield road<br>brenwick, northvale, bn4 7qt.<br>info [at] corvalehr-example [dot] com</div>
    <div class="small" style="font-weight:700;margin-top:14px">CONTACT #:</div>
    <div class="small">Tel: 00 208 771<br>Fax: 00 208 772</div>
  </div>
  <div class="vdots" style="left:399px;top:884px;height:256px"></div>
  <div class="abs cta-quote" style="left:436px;top:856px;width:300px">“IS YOUR COMPANY<br>BREAKING THE LAW?</div>
  <div class="btn-green">CALL US NOW</div>
  <div class="abs cta-quote" style="left:436px;top:1018px;width:300px">AND LET US PROTECT<br>YOUR BUSINESS”</div>
  <div class="vdots" style="left:782px;top:884px;height:256px"></div>

  <div class="abs" style="left:824px;top:856px">
    <div class="sec-title">CONTACT FORM</div>
    <div class="small" style="font-style:italic;margin-top:6px">Find out now if your business protected</div>
  </div>
  <div class="form-label" style="top:920px">Name</div>
  <div class="form-label" style="top:952px">Email</div>
  <div class="form-label" style="top:984px">Telephone</div>
  <div class="form-label" style="top:1016px">Comments</div>
  <div class="field" style="top:919px;height:24px"></div>
  <div class="field" style="top:947px;height:24px"></div>
  <div class="field" style="top:975px;height:24px"></div>
  <div class="field" style="top:1005px;height:91px"></div>
  <div class="btn-small" style="left:925px">Submit</div>
  <div class="btn-small" style="left:1031px">Clear</div>

  <footer class="footer" style="top:1183px">Copyright © 2003-2010 corvalehr-example.com. All Rights Reserved.</footer>
</section>

<section class="page page-inner">
  <header class="site-header">
    <div class="brand"><span class="brand-mark"></span><span class="brand-name">Corvale HR Ltd</span></div>
    <div class="brand-tag">Brisk HR Partner</div>
    <div class="call">Call Now: <b>000 4410 927</b></div>
    <nav class="nav">
      <a style="width:171px">HOME</a><a style="width:194px">ABOUT US</a><a style="width:231px">OUR SERVICES</a><a style="width:238px">CONTACT US</a>
    </nav>
    <div class="dropdown">
      <a>Employment Law</a><a>HR Advice</a><a>Recruitment</a><a>Disciplinaries</a><a>Redundancies</a><a>Coaching &amp; Training</a>
    </div>
  </header>

  <div class="hero" style="height:208px">
    <div class="hero-title" style="top:42px">IS YOUR COMPANY<br>LEGALLY COMPLIANT?</div>
    <div class="abs" role="img" aria-label="Group of business people standing together" style="left:542px;top:4px;width:180px;height:204px;background:linear-gradient(#6fbf4a,#2a2a2a 70%)"></div>
    <div class="abs" role="img" aria-label="Team of office staff standing in a group" style="left:940px;top:4px;width:240px;height:204px;background:linear-gradient(#8ccf5c,#3a3a3a 70%)"></div>
    <div class="abs" style="left:918px;top:159px;width:262px;text-align:right;padding-right:6px;color:#fff;font-family:'Mulish',sans-serif;font-size:23px;line-height:22px">years HR experience<br>a wealth of knowledge</div>
  </div>

  <article class="abs article" style="left:52px;top:410px;width:650px">
    <h1>Employment Law Advice</h1>
    <p>Lorem Ipsum is simply dummy text of the printing and typesetting industry. Lorem Ipsum has been the industry's standard dummy text ever since the 1500s, when an unknown printer took a galley of type and scrambled it to make a type specimen book. It has survived not only five centuries, but also the leap into electronic typesetting, remaining essentially unchanged. It was popularised in the 1960s with the release of Setrapress sheets containing Lorem Ipsum passages, and more recently with desktop publishing software like Folio Layout including versions of Lorem Ipsum.</p>
    <p>Contrary to popular belief, Lorem Ipsum is not simply random text. It has roots in a piece of classical Latin literature from 45 BC, making it over 2000 years old. Edwin Marlowe, a Latin professor at Ashgrove College in Virginia, looked up one of the more obscure Latin words, consectetur, from a Lorem Ipsum passage, and going through the cites of the word in classical literature, discovered the undoubtable source. Lorem Ipsum comes from sections 1.10.32 and 1.10.33 of "de Finibus Bonorum et Malorum" (The Extremes of Good and Evil) by Quintus Aurel, written in 45 BC. This book is a treatise on the theory of ethics, very popular during the Renaissance. The first line of Lorem Ipsum, "Lorem ipsum dolor sit amet..", comes from a line in section 1.10.32.</p>
    <p>The standard chunk of Lorem Ipsum used since the 1500s is reproduced below for those interested. Sections 1.10.32 and 1.10.33 from "de Finibus Bonorum et Malorum" by Quintus Aurel are also reproduced in their exact original form, accompanied by English versions from the 1914 translation by H. Ransford.</p>
  </article>
  <div class="vdots" style="left:735px;top:400px;height:740px"></div>

  <aside class="news">
    <h3>Latest News / Articles</h3>
    <ul>
      <li>Lorem Ipsum is simply dummy text</li>
      <li>Contrary to popular belief, Lorem Ipsum is not simply random text.</li>
      <li>The standard chunk of Lorem Ipsum used since the 1500s.</li>
      <li>This book is a treatise.</li>
    </ul>
    <span class="more">More</span>
  </aside>

  <footer class="footer" style="top:1182px;height:57px">Copyright © 2003-2010 corvalehr-example.com. All Rights Reserved.</footer>
</section>

</body>
</html>
```